Pharmacy and Travel Clinic Leaflet

We are an established pharmacy and gift shop which also runs a travel and vaccination clinic. We have had the same leaflet for a couple of years and would like to refresh it for the following reasons:
We have rebranded our travel and vaccination clinic as Fellgate Journey Clinic with its own dedicated website (www.fellgatejourneyclinic.co.uk).
We have made changes to our prices that need to be reflected in the new leaflet.

The original leaflet was a little information heavy as the service was new and we would like the new leaflet to be more visually appealing with the pharmacy side highlighting our services and using the colours of our logo (purple and green) and the vaccination side using the colours of our travel clinic logo (navy blue, light blue, red and white). Logo's are attached in a variety of formats as I have no idea what is most useful.

I will upload some images that may assist with the design, as well as updated text for the pharmacy leaflet and the new prices and text required for the vaccination side. I do not expect all of the images to be used.

The leaflet is to be two-sided, which we will print in A3 and possibly enlarge to use on a large A-Board.

I would like to receive the files in format(s) that can be sent to a printers and also added to our website to display our prices.

I have attached a copy of our existing leaflet for reference.

If any information requires clarification or there are files that you need to improve the design then please let me know and I will try to sort that out.

P.S. The font we usually use now is Orkney

I have an extra requirement if this is possible. On the pharmacy services side of the leaflet I would like the tagline Providing QRS services at the bottom right of the leaflet. It can go on the bottom left if necessary. It doesn't need to be large. It needs to be in the black font (Arial or Helvetica) with the QRS logo in blue. I have attached a link to the QRS logo website and files are now uploaded to give you an idea of what we need.
The Providing QRS services and logo need to be exactly as shown in the uploads. The QRS do not allow their logo to be used creatively.
https://www.example-qrs-health.org/qrsidentity/identity-guidelines/service-branding/

Thanks for all the submissions. They were very good but I had to choose one.

Target Market(s)

All ages from young students through to pensioners.

Industry/Entity Type

Pharmacy

Font styles to use
Sans Serif

Colors
9bcb3c
6c459b
ec1f27
0255a3
ffffff

Requirements
Must have
• Leaflet needs to be professional yet still be bold enough to stand out.
• Premium look using colours stated in brief. Colours differ for pharmacy side and travel clinic side. Please don't mix pharmacy and travel colours
Nice to have
• Please use the logos and tie the scheme in with those colours. Where the prices of vaccines are listed they need to be clear
• The Providing QRS services line and logo need to be exactly as shown in the uploads. The QRS do not allow their logo to be used creatively.
Should not have
• Must not be too informal. No comedy fonts

```html
<!DOCTYPE html>
<html lang="en">
<head>
<meta charset="utf-8">
<title>Hartwell Chemist &amp; Fellgate Journey Clinic Leaflet</title>
<link rel="stylesheet" href="https://fonts.googleapis.com/css2?family=Oswald:wght@300;400&family=Lato:wght@400;700&display=swap">
<style>
  :root{
    --purple:#6c459b;
    --purple-deep:#563583;
    --green:#8dc63f;
    --ink-purple:#3a2a55;
    --red:#ec1f27;
    --sky:#3fb7ea;
    --navy:#0255a3;
    --white:#ffffff;
    --text:#2b2b2b;
    --muted:#555555;
    --stage:#e4e4e4;
  }
  *{box-sizing:border-box;margin:0;padding:0}
  html,body{width:1200px;height:1200px;overflow:hidden}
  body{background:var(--stage);position:relative;font-family:"Lato",sans-serif;color:var(--text)}
  .page{position:absolute;top:242px;width:506px;height:716px;background:var(--white);overflow:hidden}
  .page--pharmacy{left:63px}
  .page--travel{left:633px}
  .page svg.backdrop{position:absolute;left:0;top:0;width:506px;height:716px}
  .abs{position:absolute}

  /* Pharmacy side */
  .brand-name{left:0;top:150px;width:270px;text-align:center;color:var(--white);font-family:"Lato",sans-serif;font-weight:400;font-size:22px;letter-spacing:.5px;text-transform:uppercase}
  .brand-mark{left:119px;top:110px;width:32px;height:32px;border:2px solid var(--white)}
  .headline{left:34px;top:258px;width:350px;font-family:"Oswald",sans-serif;font-weight:300;font-size:19px;line-height:22px;color:var(--ink-purple);text-transform:uppercase;letter-spacing:-.2px}
  .services{left:256px;top:330px;width:240px;list-style:none}
  .services li{position:relative;padding-left:14px;font-size:10.2px;line-height:12px;color:var(--text);margin-bottom:11.4px}
  .services li::before{content:"";position:absolute;left:0;top:2px;width:7px;height:7px;background:var(--purple)}
  .visit{left:0;top:613px;width:506px;height:59px;color:var(--white);font-family:"Oswald",sans-serif;font-weight:300;font-size:15px;text-align:center;line-height:24px;padding-top:6px}
  .contact{left:0;top:672px;width:506px;height:44px;text-align:center;line-height:44px;font-size:15px;color:var(--ink-purple)}

  /* Travel side */
  .clinic-name{left:79px;top:190px;width:120px;text-align:center;color:var(--red);font-family:"Oswald",sans-serif;font-weight:400;font-size:15px;line-height:18px;text-transform:uppercase}
  .tab{height:24px;padding:0 12px;background:var(--red);color:var(--white);border-radius:12px 12px 0 0;font-family:"Oswald",sans-serif;font-weight:300;font-size:10.5px;line-height:26px;text-transform:uppercase}
  .tab--vaccines{left:34px;top:307px;width:94px}
  .tab--malaria{left:252px;top:307px;width:95px}
  table.prices{position:absolute;border-collapse:collapse;font-size:9.3px;color:var(--text)}
  table.prices td{border:1px solid #333;padding:0 8px;line-height:11px}
  table.prices td.price{background:var(--sky);text-align:center;color:#1d1d1d;font-weight:700}
  .prices--vaccines{left:34px;top:331px;width:196px}
  .prices--vaccines td{height:16.2px}
  .prices--vaccines td.price{width:40px}
  .prices--malaria{left:252px;top:331px;width:218px}
  .prices--malaria td.price{width:91px;font-weight:400}
  .prices--malaria tr.sub td{background:var(--sky);color:var(--white);font-family:"Oswald",sans-serif;font-weight:300}
  .note{left:31px;width:320px;font-size:8.3px;line-height:11.5px;color:var(--muted)}
  .note--dose{top:527px}
  .note--stock{top:550px}
  .more{left:24px;top:656px;color:var(--white);font-family:"Oswald",sans-serif;font-weight:300;font-size:16px;text-transform:uppercase}
  .more-link{left:24px;top:683px;color:var(--white);font-weight:700;font-size:9.3px}
</style>
</head>
<body>

<section class="page page--pharmacy" aria-label="Hartwell Chemist pharmacy services">
  <svg class="backdrop" viewBox="0 0 506 716" aria-hidden="false">
    <defs>
      <linearGradient id="pillsTone" x1="0" y1="0" x2="1" y2="1">
        <stop offset="0" stop-color="#7a55a8"/><stop offset="1" stop-color="#5a3a88"/>
      </linearGradient>
      <linearGradient id="familyTone" x1="0" y1="0" x2="0" y2="1">
        <stop offset="0" stop-color="#7d7f86"/><stop offset=".45" stop-color="#c9ccd6"/><stop offset="1" stop-color="#e9ebef"/>
      </linearGradient>
      <linearGradient id="greyTone" x1="0" y1="0" x2="1" y2="0">
        <stop offset="0" stop-color="#cfcfcf"/><stop offset=".7" stop-color="#ececec"/><stop offset="1" stop-color="#ffffff"/>
      </linearGradient>
    </defs>
    <rect x="0" y="0" width="270" height="244" fill="url(#pillsTone)" role="img" aria-label="Close-up photo of tablets in blister packs under a purple tint"/>
    <rect x="278" y="8" width="106" height="118" fill="var(--purple)"/>
    <rect x="391" y="8" width="106" height="118" fill="var(--green)"/>
    <rect x="278" y="130" width="106" height="114" fill="var(--green)"/>
    <rect x="391" y="130" width="106" height="114" fill="var(--purple)"/>
    <rect x="288" y="19" width="198" height="214" fill="var(--white)"/>
    <rect x="291" y="22" width="192" height="208" fill="url(#familyTone)" role="img" aria-label="Photo of a family with colds resting together in bed"/>
    <rect x="0" y="251" width="385" height="59" fill="var(--green)"/>
    <rect x="391" y="251" width="115" height="59" fill="var(--purple)"/>
    <rect x="0" y="310" width="252" height="303" fill="url(#greyTone)" role="img" aria-label="Greyscale photo of a woman with a cold and the pharmacy delivery van"/>
    <rect x="0" y="613" width="506" height="59" fill="var(--purple)"/>
    <rect x="0" y="672" width="506" height="44" fill="var(--green)"/>
  </svg>

  <div class="abs brand-mark" aria-hidden="true"></div>
  <div class="abs brand-name">Hartwell Chemist</div>

  <h1 class="abs headline">Long-established independent pharmacy<br>offering a wide range of services including:</h1>

  <ul class="abs services">
    <li>Free prescription collection &amp; delivery service</li>
    <li>Large stocks, multiple suppliers &amp; efficient, personal service</li>
    <li>Experienced staff working with cutting edge automation</li>
    <li>Cholesterol Testing</li>
    <li>Quit Smoking Service</li>
    <li>Minor Ailments Scheme</li>
    <li>Mobility Aids</li>
    <li>Free Text Notification Service</li>
    <li>Seasonal Flu Vaccination</li>
    <li>Private vaccinations for individuals &amp; groups</li>
  </ul>

  <div class="abs visit">14 Market Row, Thornby. TB4 2QX<br>Monday to Friday: 8.30am - 6.00pm &amp; Saturday: 8.30am - 4.00pm</div>
  <div class="abs contact">www.hartwellchemist.com &nbsp;|&nbsp; 01632 960418</div>
</section>

<section class="page page--travel" aria-label="Fellgate Journey Clinic price list">
  <svg class="backdrop" viewBox="0 0 506 716">
    <defs>
      <linearGradient id="beachTone" x1="0" y1="0" x2="0" y2="1">
        <stop offset="0" stop-color="#4f9fe0"/><stop offset=".35" stop-color="#a9d6f2"/><stop offset=".6" stop-color="#4fc3d6"/><stop offset="1" stop-color="#e8efe8"/>
      </linearGradient>
      <linearGradient id="shoreTone" x1="0" y1="0" x2="0" y2="1">
        <stop offset="0" stop-color="#ffffff"/><stop offset=".5" stop-color="#c7e9f0"/><stop offset="1" stop-color="#7fcfdc"/>
      </linearGradient>
    </defs>
    <rect x="0" y="0" width="506" height="340" fill="url(#beachTone)" role="img" aria-label="Photo of a tropical beach with a palm tree and a striped hammock"/>
    <rect x="0" y="560" width="506" height="156" fill="url(#shoreTone)" role="img" aria-label="Photo of a wooden longtail boat in shallow turquoise water"/>
    <path d="M0 318 C15 280 45 245 85 236 L200 236 C300 244 390 262 506 270 L506 292 C400 292 320 276 210 270 L90 270 C55 285 25 315 0 345 Z" fill="var(--red)"/>
    <path d="M200 268 C320 276 410 300 506 286 L506 314 C410 328 310 304 200 292 Z" fill="var(--sky)"/>
    <path d="M0 345 C25 315 55 290 95 284 L200 290 C310 304 410 330 506 314 L506 560 L0 560 Z" fill="var(--white)"/>
    <circle cx="139" cy="214" r="76" fill="var(--red)"/>
    <circle cx="139" cy="214" r="70" fill="var(--sky)"/>
    <circle cx="139" cy="214" r="64" fill="var(--white)"/>
    <path d="M0 656 C80 614 190 606 258 642 L250 652 C190 622 80 628 0 664 Z" fill="var(--sky)"/>
    <path d="M0 716 L0 664 C80 628 190 622 250 652 C295 676 320 698 339 716 Z" fill="var(--red)"/>
  </svg>

  <div class="abs clinic-name">Fellgate<br>Journey Clinic</div>

  <div class="abs tab tab--vaccines">Travel Vaccines*</div>
  <table class="prices prices--vaccines">
    <tr><td>Cholera</td><td class="price">£25</td></tr>
    <tr><td>Diphtheria Tetanus and Polio</td><td class="price">£30</td></tr>
    <tr><td>Hepatitis A</td><td class="price">£40</td></tr>
    <tr><td>Hepatitis B</td><td class="price">£40</td></tr>
    <tr><td>Hepatitis A &amp; B (combined)</td><td class="price">£70</td></tr>
    <tr><td>Hepatitis A &amp; Typhoid (combined)</td><td class="price">£70</td></tr>
    <tr><td>Japanese Encephalitis</td><td class="price">£85</td></tr>
    <tr><td>Meningitis ACWY</td><td class="price">£50</td></tr>
    <tr><td>Rabies</td><td class="price">£60</td></tr>
    <tr><td>Tick Borne Encephalitis</td><td class="price">£60</td></tr>
    <tr><td>Typhoid</td><td class="price">£35</td></tr>
  </table>

  <div class="abs tab tab--malaria">Antimalarials</div>
  <table class="prices prices--malaria">
    <tr><td style="height:35px">Generic Maltavex<br>(Atovaquone/Proguanil)</td><td class="price">£2 per tablet</td></tr>
    <tr><td style="height:20px">Doxycycline 100mg</td><td class="price">50p per capsule</td></tr>
    <tr class="sub"><td style="height:18px">We also vaccinate against:</td><td></td></tr>
    <tr><td style="height:16px">Chickenpox</td><td class="price" style="font-weight:700">£60</td></tr>
    <tr><td style="height:26px">Measles Mumps &amp;<br>Rubella (MMR)</td><td class="price" style="font-weight:700">£40</td></tr>
    <tr><td style="height:16px">Meningitis B</td><td class="price" style="font-weight:700">£110</td></tr>
    <tr><td style="height:15px">Shingles</td><td class="price" style="font-weight:700">£150</td></tr>
    <tr><td style="height:25px">Human Papilloma<br>Virus (HPV)</td><td class="price" style="font-weight:700">£150</td></tr>
  </table>

  <p class="abs note note--dose">*Prices are per dose &amp; more than one dose of vaccine may be needed</p>
  <p class="abs note note--stock" style="width:240px">**The availability and price of the above may vary. During shortages wholesale prices can rise and we will inform you of any price changes.</p>

  <div class="abs more">For more information visit</div>
  <div class="abs more-link">www.fellgatejourneyclinic.co.uk or call 01632 960418</div>
</section>

</body>
</html>
```